50th Anniversary Gala Save the date Postcard 8.5x5.5 inches

Looking for a 5.5x8.5 in one-sided postcard design for our annual gala. Design needs to include "Save the date" prominently with all the event information included below. Design should be light, include the colors of our logo and elegant. (almost like a wedding save the date). "Bridges of Grace" should look like its own logo.

50th Anniversary Gala at The Lodge at Birchmere Glen – “Bridges of Grace – Celebrating 50 Years of Building Community”
Thursday, October 24
6-11p
The Lodge at Birchmere Glen
Calloway Parkway, New Hyde Park, NY
Honoring – TRB Previous Presidents

Target Market(s)

Exisiting donors

Industry/Entity Type

nonprofit

Font styles to use
Serif
Script

Requirements
Must have
• Save the date prominent
Should not have
• should not have a dark background

```html
<!DOCTYPE html>
<html lang="en">
<head>
<meta charset="utf-8">
<title>Save the Date – 50th Anniversary Gala – Bridges of Grace</title>
<link rel="stylesheet" href="https://fonts.googleapis.com/css2?family=Montserrat:ital,wght@0,300;0,400;0,700;1,300&family=Poppins:wght@400;600&family=Great+Vibes&family=Cormorant+Garamond:wght@500;600&display=swap">
<style>
  :root {
    --cream: #f8f5ec;
    --taupe: #aa937a;
    --taupe-dark: #8c7459;
    --taupe-light: #bba98f;
    --frame: #d3c5b3;
    --ornament: #e3d7c6;
    --white: #ffffff;
    --text-soft: #8f7f6c;
  }
  * { margin: 0; padding: 0; box-sizing: border-box; }
  html, body { width: 1200px; height: 807px; overflow: hidden; background: var(--cream); }
  .postcard { position: relative; width: 1200px; height: 807px; background: var(--cream); }
  .frame { position: absolute; inset: 0; }
  .ornament {
    position: absolute; width: 120px; height: 120px;
    background: radial-gradient(circle at 50% 50%, var(--ornament), rgba(227,215,198,0) 70%);
  }
  .ornament--tl { left: 20px; top: 12px; }
  .ornament--tr { right: 20px; top: 12px; }
  .ornament--bl { left: 20px; bottom: 12px; }
  .ornament--br { right: 20px; bottom: 12px; }

  .event-heading { position: absolute; left: 98px; top: 88px; width: 536px; text-align: right; color: var(--taupe-dark); }
  .event-heading__title { font-family: "Montserrat", sans-serif; font-weight: 700; font-size: 44px; letter-spacing: 0.3px; line-height: 1.1; text-align: left; }
  .event-heading__venue { font-family: "Montserrat", sans-serif; font-weight: 300; font-style: italic; font-size: 30px; line-height: 1.3; }

  .host-name { position: absolute; left: 862px; top: 62px; width: 220px; display: flex; flex-direction: column; align-items: center; gap: 12px; }
  .host-name__mark { width: 58px; height: 58px; border-radius: 50%; background: var(--taupe-light); }
  .host-name__text { font-family: "Montserrat", sans-serif; font-weight: 700; font-size: 26px; line-height: 1.15; color: var(--taupe-dark); text-align: center; text-transform: uppercase; letter-spacing: 0.5px; }

  .band-rule { position: absolute; left: 0; right: 0; height: 7px; background: var(--taupe); }
  .band-rule--top { top: 262px; }
  .band-rule--bottom { top: 549px; }
  .theme-band {
    position: absolute; left: 0; right: 0; top: 274px; height: 268px;
    background: var(--taupe); color: var(--white); text-align: center;
    display: flex; flex-direction: column; align-items: center; justify-content: center;
  }
  .theme-band__save { font-family: "Cormorant Garamond", serif; font-weight: 600; font-size: 30px; letter-spacing: 10px; text-transform: uppercase; line-height: 1; }
  .theme-band__title { font-family: "Great Vibes", cursive; font-size: 116px; font-weight: 400; line-height: 1; margin-top: 10px; }
  .theme-band__subtitle { font-family: "Cormorant Garamond", serif; font-weight: 500; font-size: 36px; line-height: 1; margin-top: 12px; }

  .event-details { position: absolute; left: 0; right: 0; top: 568px; text-align: center; }
  .event-details__date { font-family: "Poppins", sans-serif; font-weight: 600; font-size: 36px; color: var(--taupe-dark); line-height: 1.2; }
  .event-details__place { font-family: "Poppins", sans-serif; font-weight: 400; font-size: 28px; color: var(--taupe-light); line-height: 1.28; margin-top: 4px; }
  .event-details__honoring { font-family: "Montserrat", sans-serif; font-weight: 400; font-size: 24px; color: var(--text-soft); margin-top: 8px; letter-spacing: 0.4px; }
</style>
</head>
<body>
<main class="postcard">
  <svg class="frame" width="1200" height="807" viewBox="0 0 1200 807" aria-hidden="true">
    <path d="M30 258 V19 H1170 V258" fill="none" stroke="var(--frame)" stroke-width="3"/>
    <path d="M30 562 V781 H1170 V562" fill="none" stroke="var(--frame)" stroke-width="3"/>
  </svg>
  <div class="ornament ornament--tl" role="img" aria-label="Decorative filigree corner ornament"></div>
  <div class="ornament ornament--tr" role="img" aria-label="Decorative filigree corner ornament"></div>
  <div class="ornament ornament--bl" role="img" aria-label="Decorative filigree corner ornament"></div>
  <div class="ornament ornament--br" role="img" aria-label="Decorative filigree corner ornament"></div>

  <header class="event-heading">
    <h1 class="event-heading__title">50th Anniversary Gala</h1>
    <p class="event-heading__venue">at The Lodge at Birchmere Glen</p>
  </header>

  <div class="host-name">
    <span class="host-name__mark"></span>
    <span class="host-name__text">Harborlight Alliance</span>
  </div>

  <div class="band-rule band-rule--top"></div>
  <section class="theme-band">
    <p class="theme-band__save">Save the Date</p>
    <h2 class="theme-band__title">Bridges of Grace</h2>
    <p class="theme-band__subtitle">Celebrating 50 Years of Building Community</p>
  </section>
  <div class="band-rule band-rule--bottom"></div>

  <section class="event-details">
    <p class="event-details__date">Thursday, October 24, 6-11pm</p>
    <p class="event-details__place">The Lodge at Birchmere Glen<br>Calloway Parkway, New Hyde Park, NY</p>
    <p class="event-details__honoring">Honoring – TRB Previous Presidents</p>
  </section>
</main>
</body>
</html>
```